Monthly Marketing Memo needs a Letterhead

Our firm, ZOV Solutions produces "Bilal's Monthly Marketing Memo", a monthly digest of marketing tips and tips for business owners in the MENA region. We use Mailrook to distribute this memo to our database each month. We are looking for a designer to put together a letterhead for this memo.

The goal of the memo is to produce original, relevant, and new content to readers. We are a quickly adapting company. We provide fresh material, and the branding and logo of the newsletter heading should reflect this.

What the letterhead should include:
- Our ZOV Solutions logo (provided by me)
- The words "Bilal's Monthly Marketing Memo"
- Bilal's picture (provided by me)

It should be in a jpg or png format so that I can load it into the Mailrook template. The template is designed to be a traditional A4 in width.

To receive our logo and Bilal's picture for your design, please email me at dana@zovsolutions.example.

Target Market(s)

Companies in the MENA region that are looking to dramatically improve their sales and marketing.

Industry/Entity Type

Marketing

Requirements
Must have
• The letterhead must be neat and have a clean design.
Should not have
• Too many colors, swirls or soft fonts.

```html
<!DOCTYPE html>
<html lang="en">
<head>
<meta charset="utf-8">
<title>Bilal's Monthly Marketing Memo – Letterhead</title>
<link rel="stylesheet" href="https://fonts.googleapis.com/css2?family=Source+Sans+3:wght@400;600;700&display=swap">
<style>
  :root {
    --paper: #ffffff;
    --ink: #1a1a1a;
    --brand-blue: #4fb3e8;
    --brand-grey: #8a9296;
    --frame-grey: #dfe3e4;
    --photo-tone: #8e8a86;
    --photo-light: #d8d4cf;
    --signature-tone: #ececec;
  }
  html, body {
    margin: 0;
    padding: 0;
    overflow: hidden;
    background: var(--paper);
  }
  .letterhead {
    position: relative;
    width: 812px;
    height: 1200px;
    overflow: hidden;
    background: var(--paper);
    font-family: "Source Sans 3", "Myriad Pro", Arial, sans-serif;
    color: var(--ink);
  }
  .memo-mark {
    position: absolute;
    left: 18px;
    top: 0;
    width: 124px;
    height: 126px;
    background: var(--brand-blue);
  }
  .memo-title {
    position: absolute;
    left: 17px;
    top: 142px;
    margin: 0;
    font-size: 18px;
    line-height: 24px;
    color: var(--brand-grey);
  }
  .memo-title .memo-owner { display: block; font-weight: 700; }
  .memo-title .memo-name { display: block; font-weight: 400; }
  .author-photo {
    position: absolute;
    left: 545px;
    top: 0;
    width: 177px;
    height: 228px;
    box-sizing: border-box;
    border: 4px solid var(--frame-grey);
    background: linear-gradient(180deg, var(--photo-light) 0%, var(--photo-tone) 100%);
  }
  .company-name {
    position: absolute;
    left: 17px;
    top: 355px;
    margin: 0;
    font-size: 17px;
    line-height: 24px;
    font-weight: 400;
  }
  .intro {
    position: absolute;
    left: 17px;
    top: 483px;
    width: 185px;
    margin: 0;
    font-size: 12.5px;
    line-height: 20px;
    font-weight: 600;
  }
  .body-copy {
    position: absolute;
    left: 17px;
    top: 612px;
    width: 771px;
    margin: 0;
    font-size: 12.5px;
    line-height: 19.5px;
    font-weight: 600;
    text-align: justify;
  }
  .signature {
    position: absolute;
    left: 18px;
    top: 822px;
    width: 184px;
    height: 120px;
    background: var(--signature-tone);
  }
  .sign-off {
    position: absolute;
    left: 17px;
    top: 962px;
    margin: 0;
    font-size: 16px;
    line-height: 23px;
    font-weight: 600;
  }
  .footer-brand {
    position: absolute;
    left: 18px;
    top: 1145px;
    display: flex;
    align-items: center;
    gap: 12px;
  }
  .footer-brand .brand-square {
    width: 48px;
    height: 48px;
    background: var(--brand-blue);
  }
  .footer-brand .brand-name {
    font-size: 30px;
    line-height: 48px;
    font-weight: 600;
    color: var(--brand-grey);
  }
  .contact {
    position: absolute;
    left: 443px;
    top: 1128px;
    margin: 0;
    font-style: normal;
    color: var(--brand-grey);
  }
  .contact .web { display: block; font-size: 16px; line-height: 24px; }
  .contact .phone { display: block; font-size: 12.5px; line-height: 22px; }
  .contact .email { display: block; font-size: 15px; line-height: 20px; padding-left: 3px; }
</style>
</head>
<body>
<main class="letterhead">
  <header>
    <div class="memo-mark"></div>
    <h1 class="memo-title">
      <span class="memo-owner">Bilal's Monthly</span>
      <span class="memo-name">Marketing Memo</span>
    </h1>
    <div class="author-photo" role="img" aria-label="Portrait photograph of Bilal"></div>
  </header>

  <p class="company-name">ZOV Solutions</p>

  <p class="intro">Lorem ipsum dolor sit amet, consectetuer adipiscing elit.</p>

  <p class="body-copy">Lorem ipsum dolor sit amet, consectetuer adipiscing elit. Nam cursus. Morbi ut mi. Nullam enim leo, egestas id, condimentum at, laoreet mattis, massa. Sed eleifend nonummy diam. Praesent mauris ante, elementum et, bibendum at, posuere sit amet, nibh. Duis tincidunt lectus quis dui viverra vestibulum. Suspendisse vulputate aliquam dui. Nulla elementum dui ut augue. Aliquam vehicula mi at mauris. Maecenas placerat, nisl at consequat rhoncus, sem nunc gravida justo, quis eleifend arcu velit quis lacus. Morbi magna magna, tincidunt a, mattis non, imperdiet vitae, tellus. Sed odio est, auctor ac, sollicitudin in, consequat vitae, orci. Fusce id felis. Vivamus sollicitudin metus eget eros. Pellentesque habitant morbi tristique senectus et netus et malesuada fames ac turpis.</p>

  <div class="signature" role="img" aria-label="Handwritten signature"></div>

  <p class="sign-off">Zovsolutions<br>dolor sit amet,<br>917 5550 0142</p>

  <footer>
    <div class="footer-brand">
      <span class="brand-square"></span>
      <span class="brand-name">ZOV Solutions</span>
    </div>
    <address class="contact">
      <span class="web">http://zovsolutions.example</span>
      <span class="phone">United States &nbsp;&nbsp;Telephone: 300 555 01 0x - 314 555 01 27.</span>
      <span class="email">xx@zovsolutions.example</span>
    </address>
  </footer>
</main>
</body>
</html>
```